Label Design for Bra "Heron Lingerie" by Larkfield Apparel Company

The bra is packaged in a poly bag with a hanger. We require a label design for the brand name "Heron Lingerie" by Larkfield Apparel Company. The main label will be attached by a string on the bra. The size of that label will 25cm in length and 10cm wide. This is the first label the customer see's when she picks up the garment/bra. Therefore, we require an eye catching design for that. This classic full shape bra with smooth moulded double layered cups fit beautifully under t-shirts and fitted garments. The larkfield apparel company logo has been included and we would like it to feature in the label. A sample labels are also given.
Target Market(s)
Laddies 18 - 45
Industry/Entity Type
Clothing
Look and feel
Each slider illustrates characteristics of the customer's brand and the style your logo design should communicate.

```html
<!DOCTYPE html>
<html lang="en">
<head>
<meta charset="utf-8">
<title>Heron Lingerie – Hang Tag</title>
<link rel="stylesheet" href="https://fonts.googleapis.com/css2?family=Quicksand:wght@400;500;600&family=Open+Sans:ital,wght@0,400;1,700&display=swap">
<style>
  :root {
    --backdrop: #e4e4e4;
    --tag-stock: #efefef;
    --tag-edge: #d2d2d2;
    --ink: #27263a;
    --ink-soft: #3a394d;
    --band-text: #f4f4f4;
    --eyelet: #9a9a9a;
  }
  html, body {
    margin: 0;
    padding: 0;
    width: 1200px;
    height: 899px;
    overflow: hidden;
    background: var(--backdrop);
  }
  .canvas {
    position: relative;
    width: 1200px;
    height: 899px;
  }
  .tag-shape {
    position: absolute;
    left: 0;
    top: 0;
  }
  .figure-art {
    position: absolute;
    left: 452px;
    top: 338px;
    width: 112px;
    height: 372px;
    border-radius: 50px 50px 8px 8px;
    background: linear-gradient(180deg, #3b3a50 0%, #2a293c 100%);
    opacity: 0.9;
  }
  .tag-text {
    position: absolute;
    z-index: 1;
  }
  .brand-mark {
    right: 480px;
    top: 346px;
    display: flex;
    flex-direction: column;
    align-items: flex-end;
    gap: 6px;
  }
  .brand-mark__square {
    width: 26px;
    height: 26px;
    background: var(--ink);
  }
  .brand-mark__name {
    font-family: "Quicksand", sans-serif;
    font-weight: 600;
    font-size: 10px;
    color: var(--ink);
    text-align: right;
    line-height: 1.15;
    width: 90px;
  }
  .product-title {
    right: 480px;
    top: 425px;
    margin: 0;
    font-family: "Quicksand", sans-serif;
    font-weight: 500;
    font-size: 25px;
    line-height: 38px;
    letter-spacing: 0.5px;
    color: var(--ink);
    text-align: right;
    text-transform: uppercase;
  }
  .product-subtitle {
    right: 480px;
    top: 515px;
    width: 140px;
    margin: 0;
    font-family: "Open Sans", sans-serif;
    font-style: italic;
    font-weight: 700;
    font-size: 9px;
    line-height: 14px;
    color: var(--ink-soft);
    text-align: right;
  }
  .product-subtitle .keyword {
    font-style: normal;
    font-weight: 400;
    font-family: "Quicksand", sans-serif;
    font-size: 13px;
  }
  .product-copy {
    right: 480px;
    top: 584px;
    width: 112px;
    margin: 0;
    font-family: "Quicksand", sans-serif;
    font-weight: 500;
    font-size: 9.5px;
    line-height: 12.3px;
    color: var(--ink);
    text-align: right;
  }
  .feature-band {
    position: absolute;
    z-index: 2;
    left: 429px;
    top: 710px;
    width: 343px;
    height: 26px;
    background: var(--ink);
    color: var(--band-text);
    font-family: "Open Sans", sans-serif;
    font-size: 10.5px;
    line-height: 26px;
    padding-left: 31px;
    box-sizing: border-box;
  }
  .feature-band em {
    font-weight: 700;
  }
</style>
</head>
<body>
<main class="canvas">
  <svg class="tag-shape" width="1200" height="899" viewBox="0 0 1200 899" aria-hidden="true">
    <path d="M468 240 H733 L773 292 V790 H428 V292 Z" fill="var(--tag-stock)" stroke="var(--tag-edge)" stroke-width="1"/>
    <circle cx="600" cy="272" r="12" fill="var(--eyelet)"/>
    <circle cx="600" cy="272" r="6" fill="var(--backdrop)"/>
  </svg>

  <div class="figure-art" role="img" aria-label="Silhouette illustration of a woman in a fitted dress and heels"></div>

  <div class="tag-text brand-mark">
    <span class="brand-mark__square"></span>
    <span class="brand-mark__name">larkfield apparel company</span>
  </div>

  <h1 class="tag-text product-title">Heron<br>Lingerie</h1>

  <p class="tag-text product-subtitle">Classic Full Shape <span class="keyword">Bra</span> with<br>Smooth Moulded Double<br>Layered Cups</p>

  <p class="tag-text product-copy">Lorem ipsum dolor sit amet, consectetur adipisicing elit, sed do eiusmod tempor incididunt ut labore et dolore magna aliqua. Ut enim ad minim veniam, quis nostrud exercitation.</p>

  <div class="feature-band"><em>Fits Beautifully</em> under T-Shirts and Fitted Garments</div>
</main>
</body>
</html>
```